Velvet Bloom Marisol's Cleaning Service Business Cards Project

A business card with all contact details with logo design on there (already have a logo) eye catching Logo and contact info on one side, full logo on the back, must target upper class residential and corporate companies, fitness companies, still keep it on the feminine side of things , must look elegant

Target Market(s)

Upper class homes and corporate companies

Industry/Entity Type

Cleaning Service

Contact Information for Business Card

Name: Marisol Denhart
Position: Director
ABN: 47193062857
Email: marisolsvelvetcleaning@brightmail.example
Number: 0418926547

Font styles to use
Decorative

Colors

Designer to choose colors to be used in the design.

Requirements
Must have
• Available Sydney Wide, contact info and logo on one side, full logo on the back
Nice to have
• Professional appearance
Should not have
• Cheap advert looking stuff

```html
<!DOCTYPE html>
<html lang="en">
<head>
<meta charset="utf-8">
<title>Velvet Bloom – Business Cards</title>
<link rel="stylesheet" href="https://fonts.googleapis.com/css2?family=Cinzel:wght@700&family=Jost:wght@400;500&display=swap">
<style>
  :root {
    --page: #1f2026;
    --card: #2b2f3e;
    --card-deep: #262a37;
    --teal: #40dccb;
    --teal-soft: #7ff0e2;
    --ink: #e3e6ee;
    --muted: #b9bdc9;
    --rule: #8d93a3;
  }
  * { box-sizing: border-box; margin: 0; padding: 0; }
  html, body {
    width: 1200px;
    height: 960px;
    overflow: hidden;
    background: var(--page);
  }
  .sheet {
    position: relative;
    width: 1200px;
    height: 960px;
  }
  .card {
    position: absolute;
    left: 240px;
    width: 720px;
    height: 412px;
    background: linear-gradient(160deg, var(--card) 0%, var(--card-deep) 100%);
    overflow: hidden;
  }
  .card--back { top: 48px; }
  .card--front { top: 500px; }

  /* Back */
  .back-mark {
    position: absolute;
    left: 0; right: 0; top: 120px;
    display: flex;
    flex-direction: column;
    align-items: center;
    gap: 18px;
  }
  .mark-dot {
    width: 18px; height: 18px;
    border-radius: 50%;
    background: var(--teal);
  }
  .brand-name {
    font-family: "Cinzel", serif;
    font-weight: 700;
    color: var(--teal);
    letter-spacing: 3px;
    text-transform: uppercase;
    text-align: center;
  }
  .back-mark .brand-name { font-size: 44px; line-height: 1; }
  .back-web {
    position: absolute;
    left: 0; right: 0; top: 300px;
    text-align: center;
    font-family: "Jost", sans-serif;
    font-size: 15px;
    letter-spacing: 4px;
    color: var(--ink);
  }

  /* Front */
  .person {
    position: absolute;
    left: 58px; top: 140px;
  }
  .person-name {
    font-family: "Cinzel", serif;
    font-weight: 700;
    font-size: 22px;
    color: var(--teal);
    letter-spacing: 1px;
    text-transform: uppercase;
  }
  .person-role {
    font-family: "Cinzel", serif;
    font-weight: 700;
    font-size: 14px;
    color: var(--ink);
    letter-spacing: 1px;
    text-transform: uppercase;
    margin-top: 2px;
  }
  .divider {
    position: absolute;
    left: 58px; right: 58px; top: 212px;
    height: 1px;
    background: var(--rule);
  }
  .contacts {
    position: absolute;
    left: 58px; top: 226px;
    list-style: none;
    font-family: "Jost", sans-serif;
    font-size: 15px;
    color: var(--ink);
  }
  .contacts li {
    display: flex;
    align-items: center;
    gap: 10px;
    height: 23px;
  }
  .contacts svg { width: 13px; height: 13px; fill: var(--teal); flex: none; }

  .front-mark {
    position: absolute;
    right: 58px; top: 90px;
    width: 260px;
    display: flex;
    flex-direction: column;
    align-items: center;
    gap: 10px;
  }
  .front-mark .brand-name { font-size: 26px; line-height: 1.15; }
  .front-mark .brand-tag { font-size: 10px; letter-spacing: 3px; }

  .abn {
    position: absolute;
    right: 58px; bottom: 44px;
    font-family: "Jost", sans-serif;
    font-size: 16px;
    letter-spacing: 1px;
    color: var(--muted);
  }
  .edge-band {
    position: absolute;
    left: 0; right: 0; bottom: 0;
    height: 12px;
    background: linear-gradient(180deg, var(--teal-soft), var(--teal));
  }
</style>
</head>
<body>
<main class="sheet">

  <section class="card card--back" aria-label="Card back">
    <div class="back-mark">
      <span class="mark-dot"></span>
      <p class="brand-name">Velvet Bloom</p>
    </div>
    <p class="back-web">www.velvetbloom.example</p>
  </section>

  <section class="card card--front" aria-label="Card front">
    <div class="person">
      <h1 class="person-name">Marisol Denhart</h1>
      <p class="person-role">Director</p>
    </div>
    <div class="divider"></div>
    <ul class="contacts">
      <li>
        <svg viewBox="0 0 24 24" aria-hidden="true"><path d="M6.6 10.8a15.1 15.1 0 0 0 6.6 6.6l2.2-2.2a1 1 0 0 1 1-.25 11.4 11.4 0 0 0 3.6.57 1 1 0 0 1 1 1V20a1 1 0 0 1-1 1A17 17 0 0 1 3 4a1 1 0 0 1 1-1h3.5a1 1 0 0 1 1 1c0 1.25.2 2.45.57 3.57a1 1 0 0 1-.25 1z"/></svg>
        0418926547
      </li>
      <li>
        <svg viewBox="0 0 24 24" aria-hidden="true"><path d="M2 5h20v14H2z M3 6l9 7 9-7" /></svg>
        marisolsvelvetcleaning@brightmail.example
      </li>
      <li>
        <svg viewBox="0 0 24 24" aria-hidden="true"><circle cx="12" cy="12" r="10"/></svg>
        www.velvetbloom.example
      </li>
    </ul>

    <div class="front-mark">
      <span class="mark-dot"></span>
      <p class="brand-name">Velvet Bloom<br><span class="brand-tag">Marisol's Cleaning Service</span></p>
    </div>

    <p class="abn">ABN: 47193062857</p>
    <div class="edge-band"></div>
  </section>

</main>
</body>
</html>
```